Velvet Lantern Distillery

I need a label designed for my small distillery. I’d like it to have a rose, and the name velvet lantern in script writing. I need the graphic to fit a standard gin bottle and I’ll need to be able to edit it depending on alcohol, warning and descriptions. I want it to look elegant and attractive, but slightly daring too. It’s a 700ml oslo bottle
Target Market(s)
Bespoke gin and vodka drinkers
Industry/Entity Type
Beverage
Font styles to use
Script
Other font styles liked:
- Something easy to read
Requirements
Must have
- Room for me to add and remove text depending on the drink
Nice to have
- Velvet lantern in script, slight colour on the rose and black writing

```html
<!DOCTYPE html>
<html lang="en">
<head>
<meta charset="utf-8">
<title>Velvet Lantern Gin Label</title>
<link href="https://fonts.googleapis.com/css2?family=Rye&family=Playfair+Display:wght@700&display=swap" rel="stylesheet">
<style>
  :root {
    --backdrop: #eeeeee;
    --label-white: #fbfbfb;
    --gold: #a88a4a;
    --gold-band: #9c7b3c;
    --pinstripe: #c8414b;
    --rose-red: #a3222a;
    --ink: #1e1e1e;
  }
  html, body {
    margin: 0;
    width: 1200px;
    height: 1200px;
    overflow: hidden;
    background: var(--backdrop);
  }
  .label-canvas {
    display: block;
    width: 1200px;
    height: 1200px;
  }
  .label-body { fill: var(--label-white); }
  .label-frame { fill: none; stroke: var(--gold); stroke-width: 3; }
  .name-band { fill: var(--gold-band); }
  .band-edge { fill: none; stroke: var(--ink); stroke-width: 2; }
  .band-pinstripe { fill: none; stroke: var(--pinstripe); stroke-width: 3; }
  .rose-cluster { fill: var(--rose-red); }
  .brand-name {
    font-family: "Rye", serif;
    font-size: 64px;
    fill: var(--ink);
    letter-spacing: 2px;
  }
  .spirit-type {
    font-family: "Playfair Display", serif;
    font-weight: 700;
    font-size: 46px;
    fill: var(--ink);
    letter-spacing: 12px;
  }
</style>
</head>
<body>
<svg class="label-canvas" viewBox="0 0 1200 1200" xmlns="http://www.w3.org/2000/svg">
  <defs>
    <clipPath id="label-shape">
      <path d="M100,420 L600,290 L1100,420 L1100,780 L600,910 L100,780 Z"/>
    </clipPath>
  </defs>

  <path class="label-body" d="M100,420 L600,290 L1100,420 L1100,780 L600,910 L100,780 Z"/>
  <path class="label-frame" d="M114,430 L600,306 L1086,430 L1086,770 L600,894 L114,770 Z"/>

  <g class="name-ribbon" clip-path="url(#label-shape)">
    <polygon class="name-band" points="100,615 1100,440 1100,610 100,785"/>
    <polygon class="band-edge" points="100,615 1100,440 1100,610 100,785"/>
    <line class="band-pinstripe" x1="100" y1="632" x2="1100" y2="457"/>
    <line class="band-pinstripe" x1="100" y1="768" x2="1100" y2="593"/>
  </g>

  <ellipse class="rose-cluster" cx="600" cy="455" rx="125" ry="82"
           role="img" aria-label="Illustration of three red roses"/>

  <g class="brand-lockup" transform="rotate(-9.93 600 612)">
    <text class="brand-name" x="560" y="600" text-anchor="middle">VELVET</text>
    <text class="brand-name" x="640" y="672" text-anchor="middle">LANTERN</text>
  </g>

  <text class="spirit-type" x="606" y="852" text-anchor="middle">GIN</text>
</svg>
</body>
</html>
```